Book Cover for College Series

We need an e-book cover design for a collection of poetry entitled, "Chalk Lanterns Vol. 1: The Heartland." Although the price is set to $200, whomever I select for this project will be used for the next three volumes of the series in the future. So be sure to have contact information ready if selected.
If selected, we can be reached at BrightQuillPress@mailnest.example
Be sure to check out the Look and Feel Slider. We would like it to come across as serious and professional, yet very personable and modern.
Target Market(s)
Target market is both current college students as well as former college students (University alums). However, on some level it is marketed towards anyone associated with universities, including professors, as well as poetry readers. Which is why, although personable, We need the look to have a serious feel to it as well.
Industry/Entity Type
College
Requirements
Must have
- The title of the book: "Chalk Lanterns: Vol 1. The Heartland"
- Be sure to have the author's name: Benedict Marlow Tesh
Nice to have
- - Nice to have a design that somehow gives off the feeling of nostalgia.
Optional: Underneath the title, include "A collection of poetry celebrating the top universities of the Midwest."
- Only include the following if it does not get in the way of the feel/look of the cover: Have the initials: B.M.T. on the left-hand corner. An example of how this should appear is in the photo attached However, it does not necessarily need to be this big.

```html
<!DOCTYPE html>
<html lang="en">
<head>
<meta charset="utf-8">
<title>Chalk Lanterns: Vol 1. The Heartland — Book Cover</title>
<link rel="stylesheet" href="https://fonts.googleapis.com/css2?family=Junge&display=swap">
<style>
  :root {
    --sky-top: #1d3556;
    --sky-mid: #35618a;
    --sky-low: #6e8fa6;
    --glow: #f3c676;
    --glow-deep: #c98a2e;
    --ground: #120c19;
    --ink: #ffffff;
    --gold: #eaa938;
  }
  * { margin: 0; padding: 0; box-sizing: border-box; }
  html, body {
    width: 900px;
    height: 1200px;
    overflow: hidden;
    background: var(--ground);
  }
  .cover {
    position: relative;
    width: 900px;
    height: 1200px;
    overflow: hidden;
    font-family: "Junge", Georgia, serif;
    color: var(--ink);
  }
  .sky-photo {
    position: absolute;
    inset: 0;
    background:
      radial-gradient(ellipse 520px 200px at 170px 880px, rgba(255, 232, 170, 0.95), rgba(243, 198, 118, 0.55) 45%, rgba(243, 198, 118, 0) 100%),
      radial-gradient(ellipse 700px 260px at 400px 780px, rgba(201, 138, 46, 0.55), rgba(201, 138, 46, 0) 100%),
      radial-gradient(ellipse 420px 300px at 170px 420px, rgba(20, 22, 36, 0.75), rgba(20, 22, 36, 0) 100%),
      linear-gradient(to bottom,
        var(--sky-top) 0%,
        var(--sky-mid) 28%,
        var(--sky-low) 48%,
        #5a5566 62%,
        #8b7152 72%,
        var(--glow-deep) 76%,
        #3a2a2a 79%,
        var(--ground) 82%,
        var(--ground) 100%);
  }
  .title {
    position: absolute;
    right: 88px;
    top: 62px;
    text-align: right;
    font-weight: 400;
    line-height: 1;
  }
  .title-series {
    display: block;
    font-size: 56px;
  }
  .title-volume {
    display: block;
    margin-top: 28px;
    font-size: 84px;
  }
  .subtitle {
    position: absolute;
    right: 88px;
    top: 430px;
    text-align: right;
    font-size: 32px;
    line-height: 71px;
  }
  .initials {
    position: absolute;
    left: 70px;
    top: 1058px;
    font-size: 40px;
    color: var(--gold);
  }
  .author {
    position: absolute;
    right: 85px;
    top: 1058px;
    font-size: 40px;
  }
</style>
</head>
<body>
  <main class="cover">
    <div class="sky-photo" role="img" aria-label="Photograph of a Midwestern sunset sky with dark clouds over a silhouetted tree line"></div>
    <h1 class="title">
      <span class="title-series">Chalk Lanterns: Vol 1.</span>
      <span class="title-volume">The Heartland</span>
    </h1>
    <p class="subtitle">A collection of poetry<br>celebrating the top universities<br>of the Midwest.</p>
    <p class="initials">B.M.T</p>
    <p class="author">Benedict Marlow Tesh</p>
  </main>
</body>
</html>
```